Banner Image for website - New Product Alert

New banner image introducing New Product Alert
Shampoo and Conditioner product should be same size on banner

Website where banner will be added is www.quenbyprivatelabel.example

Private Label
Moisturizing Shampoo and Conditioner

Target Market(s)

Current Customers and new customers

Industry/Entity Type

Beauty Salon

Number of Pages Required

1 page

Requirements
Must have
• Images of new product
New Product Alert!
CTA - Buy Samples
Highlight 1 or 2 benefits of Shampoo and Conditioner
See attachment

```html
<!DOCTYPE html>
<html lang="en">
<head>
<meta charset="utf-8">
<title>New Product Alert – Sulfate Free Moisturizing Shampoo and Conditioner</title>
<link rel="stylesheet" href="https://fonts.googleapis.com/css2?family=Cinzel:wght@400&family=Great+Vibes&family=Didact+Gothic&family=Open+Sans:wght@700&display=swap">
<style>
  :root {
    --bg-deep: #1f0b33;
    --bg-mid: #3a1561;
    --bg-glow: #5b24a3;
    --frame: #e9e4f0;
    --headline: #ffffff;
    --script: #b8a7c6;
    --benefit: #f3effa;
    --tick: #b9a9cf;
    --cta-bg: #5a2aa0;
    --cta-text: #ffffff;
    --bottle-light: #f7f5ee;
    --bottle-shade: #dcd9cf;
    --cap: #111111;
  }
  html, body {
    margin: 0;
    padding: 0;
    width: 1200px;
    height: 529px;
    overflow: hidden;
  }
  .banner {
    position: relative;
    width: 1200px;
    height: 529px;
    overflow: hidden;
    background:
      radial-gradient(ellipse 520px 420px at 1010px 300px, rgba(120, 60, 200, 0.55), transparent 70%),
      radial-gradient(ellipse 700px 380px at 650px 560px, rgba(90, 40, 160, 0.5), transparent 70%),
      linear-gradient(100deg, var(--bg-deep) 0%, var(--bg-mid) 45%, var(--bg-glow) 100%);
  }
  .offer-frame {
    position: absolute;
    left: 85px;
    top: 133px;
    width: 514px;
    height: 261px;
    box-sizing: border-box;
    border: 2px solid var(--frame);
    border-top: none;
  }
  .offer-frame::before,
  .offer-frame::after {
    content: "";
    position: absolute;
    top: 0;
    height: 2px;
    background: var(--frame);
  }
  .offer-frame::before { left: -2px; width: 86px; }
  .offer-frame::after { right: -2px; width: 82px; }
  .offer-script {
    position: absolute;
    left: 85px;
    width: 514px;
    top: 88px;
    margin: 0;
    text-align: center;
    font-family: "Great Vibes", cursive;
    font-weight: 400;
    font-size: 64px;
    line-height: 1;
    color: var(--script);
    letter-spacing: 1px;
  }
  .offer-title {
    position: absolute;
    left: 85px;
    width: 514px;
    top: 172px;
    margin: 0;
    text-align: center;
    font-family: "Cinzel", serif;
    font-weight: 400;
    font-size: 35px;
    line-height: 42px;
    color: var(--headline);
    letter-spacing: 0.5px;
  }
  .benefits {
    position: absolute;
    left: 210px;
    top: 266px;
    margin: 0;
    padding: 0;
    list-style: none;
    font-family: "Didact Gothic", sans-serif;
    font-size: 19px;
    line-height: 28px;
    color: var(--benefit);
  }
  .benefits li {
    display: flex;
    align-items: center;
    gap: 12px;
  }
  .benefits svg { flex: none; }
  .cta {
    position: absolute;
    left: 271px;
    top: 334px;
    width: 138px;
    height: 36px;
    display: flex;
    align-items: center;
    justify-content: center;
    background: var(--cta-bg);
    color: var(--cta-text);
    font-family: "Open Sans", sans-serif;
    font-weight: 700;
    font-size: 12px;
    letter-spacing: 0.3px;
    text-decoration: none;
  }
  .product {
    position: absolute;
    top: 22px;
    width: 120px;
    height: 478px;
    border-radius: 22px 22px 10px 10px;
    background: linear-gradient(90deg, var(--bottle-shade) 0%, var(--bottle-light) 35%, var(--bottle-light) 70%, var(--bottle-shade) 100%);
  }
  .product-shampoo { left: 764px; }
  .product-conditioner { left: 911px; }
</style>
</head>
<body>
  <main class="banner">
    <div class="offer-frame"></div>
    <p class="offer-script">Sulfate Free</p>
    <h1 class="offer-title">Moisturizing Shampoo<br>and Conditioner</h1>
    <ul class="benefits">
      <li>
        <svg width="19" height="19" viewBox="0 0 20 20" aria-hidden="true">
          <circle cx="10" cy="10" r="8.5" fill="none" stroke="var(--tick)" stroke-width="1.5"/>
          <path d="M6 10.3l2.8 2.8L14.5 7" fill="none" stroke="var(--tick)" stroke-width="1.6" stroke-linecap="round" stroke-linejoin="round"/>
        </svg>
        Anti-fade color protection
      </li>
      <li>
        <svg width="19" height="19" viewBox="0 0 20 20" aria-hidden="true">
          <circle cx="10" cy="10" r="8.5" fill="none" stroke="var(--tick)" stroke-width="1.5"/>
          <path d="M6 10.3l2.8 2.8L14.5 7" fill="none" stroke="var(--tick)" stroke-width="1.6" stroke-linecap="round" stroke-linejoin="round"/>
        </svg>
        Increase luster &amp; Detangles
      </li>
    </ul>
    <a class="cta" href="#">BUY SAMPLES</a>
    <div class="product product-shampoo" role="img" aria-label="Product photo: 8 fl oz bottle of sulfate-free moisturizing shampoo with black cap and private label"></div>
    <div class="product product-conditioner" role="img" aria-label="Product photo: 8 fl oz bottle of sulfate-free conditioner with black cap and private label"></div>
  </main>
</body>
</html>
```